Tobias Wrenfield - Cinematographer

NEED:
I'm looking for a sleek, professional, modern business card that will give give the recipient the impression that they can trust their production will go smoothly by hiring me. I will bring creativity and knowledge to their shoot, so that we can create powerful images.
I am looking for a card with a strong style and design ethos that could be expanded to a website and a full visual/graphic/design entity for me.
ABOUT ME:
I am a mid-twenties cinematographer, I work on music video, narrative short, commercial, and corporate projects. I blend the science and artistry of cameras and filmmaking to tell a story. I'm an artist, a technician, and a manager.
DESIGN:
I like sleek, simple design. Black, dark grays, white, dark navy, steel blues, I love cyan, but also cyan and red. I am not a fan of earthy tones. I generally prefer modern, san-serif fonts over serifs. My old logo was based on an aperture, a multi-blade device at the back of a lens that controls how much light passes through, but I made it with so many colors, that it doesn't necessarily lend itself to a specific color-scheme or design ethos. I liked that the aperture design provided a sense of the technical requirements of my job. I'm a fan of matte business cards, but am open to plenty of specialty print processes to make an outstanding card.
ATTACHED FILES:
My Old Rainbox Aperture Logo, plus a few designs I've tried playing around with, but am not tied to. I AM OPEN TO NEW DESIGNS, DO NOT FEEL TIED TO THIS.
**I've pulled my old logo down from the attached files, and instead attached other business cards I like, so as not to mislead you where I would like to go.
INFO:
Name: Tobias Wrenfield
Job: Cinematographer
Email: tkwrenfield@quillbox.example
Phone: 503.618.2907
Website: tobiaswrenfield.example
Updates
I'm adding some images of other cards that I like, and removing my old logo, since I'm looking for something new, and don't want that old logo to push anyone a certain direction.

```html
<!DOCTYPE html>
<html lang="en">
<head>
<meta charset="utf-8">
<title>Tobias Wrenfield – Cinematographer Business Card</title>
<link rel="stylesheet" href="https://fonts.googleapis.com/css2?family=Arimo:ital,wght@0,400;0,700;1,700&display=swap">
<style>
  :root {
    --page: #ffffff;
    --ink-grey: #555555;
    --ink-dark: #3a3a3a;
    --strip-light: #e9e7e8;
    --strip-mid: #b9b9b9;
    --strip-dark: #1c1c1c;
    --card-w: 726px;
    --card-h: 401px;
  }
  * { box-sizing: border-box; margin: 0; padding: 0; }
  html, body {
    width: 942px;
    height: 1200px;
    overflow: hidden;
    background: var(--page);
  }
  .sheet {
    position: relative;
    width: 942px;
    height: 1200px;
    font-family: "Arimo", Arial, sans-serif;
  }
  .card {
    position: absolute;
    left: 108px;
    width: var(--card-w);
    height: var(--card-h);
    overflow: hidden;
  }
  .card--front { top: 56px; }
  .card--back  { top: 678px; }

  /* Front */
  .film-strip-art {
    position: absolute;
    inset: 0;
    background:
      linear-gradient(180deg,
        var(--strip-dark) 0%,
        var(--strip-mid) 6%,
        var(--strip-light) 14%,
        var(--strip-light) 78%,
        var(--strip-mid) 88%,
        var(--strip-dark) 100%);
  }
  .front-title {
    position: absolute;
    left: 10px;
    top: 87px;
    font-size: 26px;
    font-weight: 700;
    letter-spacing: -0.2px;
    color: var(--ink-grey);
    text-transform: uppercase;
  }
  .front-name {
    position: absolute;
    left: 460px;
    width: 220px;
    top: 216px;
    text-align: center;
    font-size: 30px;
    line-height: 37px;
    font-weight: 400;
    color: var(--ink-grey);
    text-transform: uppercase;
  }

  /* Back */
  .card--back {
    background: conic-gradient(from 0deg at 51% 50%,
      #6e6e6e 0deg,
      #1c1c1c 50deg,
      #050505 132deg,
      #ffffff 132deg,
      #dadada 180deg,
      #b0b0b0 240deg,
      #9d9d9d 300deg,
      #8a8a8a 340deg,
      #6e6e6e 360deg);
  }
  .back-name {
    position: absolute;
    left: 26px;
    top: 222px;
    font-size: 23px;
    font-weight: 700;
    font-style: italic;
    font-variant: small-caps;
    color: var(--ink-dark);
  }
  .contact-list {
    position: absolute;
    left: 48px;
    top: 277px;
    list-style: none;
  }
  .contact-list li {
    font-size: 13px;
    font-weight: 700;
    letter-spacing: 1.2px;
    color: var(--ink-dark);
    text-transform: uppercase;
    line-height: 13px;
    margin-bottom: 22px;
  }
</style>
</head>
<body>
  <main class="sheet">
    <section class="card card--front">
      <div class="film-strip-art" role="img" aria-label="Curving strip of cinema film with sprocket holes across a light frame"></div>
      <p class="front-title">Cinematographer</p>
      <p class="front-name">Tobias<br>Wrenfield</p>
    </section>

    <section class="card card--back">
      <p class="back-name">Tobias Wrenfield</p>
      <ul class="contact-list">
        <li class="contact-phone">503.618.2907</li>
        <li class="contact-email">tkwrenfield@quillbox.example</li>
        <li class="contact-web">www.tobiaswrenfield.example</li>
      </ul>
    </section>
  </main>
</body>
</html>
```